Cloud Hosting Provider Web Site

We need to create the design for Nimbo-Pails.net a new Cloud Hosting Provider Website.

We already have a logo and a draft website with preliminary content showing the desired structure for the final web site.

I need a design for the Home Page and all 10 Internal web pages currently linked from the draft home page.

The documentation site (/docs) Customer Portal (/portal) and Support site (/support) are not part of this design project.

We need images to illustrate all pages which of course need to be consistent with the content. Please read carefully the text of each page in the draft web site to understand the purpose of each page and illustrate it accordingly.

All pages must be illustrated with images, I do not want any single page with just text.

I want to maintain the slides idea of the draft website home page.

The web site must look professional, we are competitors of huge companies like tallow grid systems (tgs.tallowgrid.com), Velquist Oriel (oriel.velquist.com) and DuneLoft (www.duneloft.com) so we need to look as serious as them.

You may download the draft web site pages to style them, I need fully finalized HTML / CSS and image files.

A top link bar and link footer must be included in every page.

Also the web site will have the possibility to start a chat conversation with a sales agent, so a graphical link to do so must be included in the design, together with a chat window design (including HTML/CSS)

Information for accessing the draft web site follows:

URL: www.nimbo-pails.net
username: design
password: QOPqop987654

If you need any additional information please let me know.

```html
<!DOCTYPE html>
<html lang="en">
<head>
<meta charset="utf-8">
<title>Nimbo-Pails.net — Private Cloud Hosting</title>
<link rel="stylesheet" href="https://fonts.googleapis.com/css2?family=Roboto+Condensed:wght@400;700&family=Montserrat:wght@700&family=PT+Sans:wght@400;700&family=Cabin:wght@600;700&family=Open+Sans:wght@400;700&display=swap">
<style>
  :root {
    --page-bg: #e6e7e9;
    --panel: #ffffff;
    --ink-navy: #1b2f6a;
    --band-navy: #17164d;
    --band-glow: #1d6fc4;
    --accent-blue: #2b8fd2;
    --sky: #27a6e8;
    --tick-green: #5fc42a;
    --label-ink: #333333;
    --white: #ffffff;
    --input-bg: #0b1a3a;
  }
  * { box-sizing: border-box; margin: 0; padding: 0; }
  html, body { width: 854px; height: 1200px; overflow: hidden; }
  body { background: var(--page-bg); position: relative; font-family: "PT Sans", sans-serif; }

  .page { position: absolute; left: 10px; top: 10px; width: 834px; height: 1180px; background: var(--panel); overflow: hidden; }

  /* Header */
  .hero { position: absolute; left: 0; top: 0; width: 834px; height: 428px;
    background: radial-gradient(ellipse at 62% 45%, #f4f6fa 0%, #cdd5df 40%, #8d9db3 75%, #6c7f99 100%); }
  .hero-fade { position: absolute; left: 0; top: 0; width: 834px; height: 130px;
    background: linear-gradient(#ffffff 0%, rgba(255,255,255,.85) 45%, rgba(255,255,255,0) 100%); }
  .brand { position: absolute; left: 14px; top: 80px; font-family: "Cabin", sans-serif; font-weight: 600;
    font-size: 19px; color: var(--ink-navy); letter-spacing: -.2px; }
  .brand-dot { position: absolute; left: 52px; top: 22px; width: 50px; height: 50px; border-radius: 50%; background: var(--accent-blue); }

  .chat-link { position: absolute; left: 662px; top: 15px; width: 160px; height: 48px; text-decoration: none; }
  .chat-link .agent { position: absolute; left: 0; top: 2px; width: 46px; height: 46px; border-radius: 50%;
    background: radial-gradient(circle at 50% 40%, #e9d6c8, #8aa8c4); border: 2px solid #fff; box-shadow: 0 0 0 1px #9bb7d2; }
  .chat-link .box { position: absolute; left: 42px; top: 10px; width: 117px; height: 34px; background: var(--sky); border-radius: 2px; }
  .chat-link .q { position: absolute; left: 56px; top: 12px; width: 100px; text-align: center; font-family: "Roboto Condensed", sans-serif;
    font-size: 12.5px; color: #fff; }
  .chat-link .pill { position: absolute; left: 62px; top: 30px; width: 94px; height: 14px; background: #fff; border-radius: 7px;
    font-family: "Roboto Condensed", sans-serif; font-weight: 700; font-size: 9.5px; color: var(--ink-navy); text-align: center; line-height: 14px; }

  .top-nav { position: absolute; right: 16px; top: 82px; display: flex; gap: 9px; font-family: "Roboto Condensed", sans-serif;
    font-size: 11px; color: var(--ink-navy); letter-spacing: .1px; }
  .top-nav a { color: inherit; text-decoration: none; }
  .top-nav .sep { color: var(--ink-navy); }

  .hero-title { position: absolute; left: 0; width: 834px; text-align: center; color: #fff; font-family: "Roboto Condensed", sans-serif;
    text-shadow: 0 0 3px #000, 0 1px 2px #000; transform: scaleX(.86); }
  .hero-title.main { top: 312px; font-size: 38px; }
  .hero-title.sub { top: 352px; font-size: 28px; }

  /* Feature band */
  .band { position: absolute; left: 0; top: 428px; width: 834px; height: 263px; background:
    radial-gradient(ellipse 110px 80px at 164px 30px, rgba(40,130,220,.55), transparent),
    radial-gradient(ellipse 110px 80px at 442px 30px, rgba(40,130,220,.55), transparent),
    radial-gradient(ellipse 110px 80px at 719px 30px, rgba(40,130,220,.55), transparent),
    var(--band-navy); }
  .badge { position: absolute; top: -23px; width: 54px; height: 54px; border-radius: 50%; background: #0c0c24;
    border: 3px solid #fff; box-shadow: 0 0 0 2px var(--band-glow); }
  .badge svg { position: absolute; left: 9px; top: 9px; }
  .feature h2 { position: absolute; width: 250px; text-align: center; color: #fff; font-family: "Montserrat", sans-serif;
    font-size: 14px; line-height: 16px; top: 62px; }
  .feature ul { position: absolute; top: 110px; list-style: none; color: #fff; font-size: 12.5px; line-height: 14.8px; }
  .feature li { position: relative; padding-left: 26px; }
  .tk { position: absolute; left: 0; top: 0; }

  /* Service tiles */
  .tiles { position: absolute; left: 0; top: 691px; width: 834px; height: 249px; background: #fff; }
  .tile { position: absolute; top: 38px; width: 128px; text-align: center; }
  .tile .frame { margin: 0 auto; width: 72px; height: 72px; border: 2px solid var(--accent-blue); border-radius: 3px; background: #fff;
    box-shadow: 0 1px 2px rgba(0,0,0,.15); position: relative; }
  .tile .frame svg { position: absolute; left: 5px; top: 11px; }
  .tile p { margin-top: 10px; font-family: "Cabin", sans-serif; font-weight: 700; font-size: 15px; line-height: 15.6px; color: var(--label-ink); }

  /* Footer */
  .site-footer { position: absolute; left: 0; top: 930px; width: 834px; height: 213px; color: #fff; font-family: "Open Sans", sans-serif;
    background: radial-gradient(ellipse 420px 150px at 420px 200px, #137bd0 0%, rgba(19,123,208,.4) 50%, transparent 80%), var(--band-navy); }
  .site-footer h3 { position: absolute; top: 33px; font-size: 10.5px; font-weight: 700; color: var(--sky); }
  .about { position: absolute; left: 36px; top: 54px; width: 170px; font-size: 8.6px; line-height: 13.6px; }
  .foot-nav { position: absolute; left: 244px; top: 54px; list-style: none; font-size: 8.6px; line-height: 15px; }
  .field { position: absolute; left: 369px; width: 156px; height: 18px; background: var(--input-bg); border: 1px solid #2b4a7a;
    font-size: 9px; font-weight: 700; padding: 3px 12px; }
  .send { position: absolute; left: 369px; top: 174px; width: 76px; height: 28px; background: #050505; border: 2px solid #fff;
    font-size: 11px; font-weight: 700; text-align: center; line-height: 24px; }
  .contact { position: absolute; left: 565px; list-style: none; font-size: 8.6px; line-height: 10.5px; }
  .contact svg { position: absolute; left: -17px; top: 0; }
  .social { position: absolute; left: 583px; top: 124px; display: flex; gap: 4px; }
  .social span { width: 16px; height: 16px; border-radius: 50%; background: var(--sky); }
  .foot-brand { position: absolute; left: 703px; top: 120px; font-family: "Cabin", sans-serif; font-weight: 600; font-size: 12px; color: #2a5f9a; }
  .foot-brand-dot { position: absolute; left: 731px; top: 82px; width: 34px; height: 34px; border-radius: 50%; background: #1f5f9c; opacity: .8; }

  .copyright { position: absolute; left: 0; top: 1156px; width: 834px; text-align: center; font-family: "Open Sans", sans-serif;
    font-size: 7.6px; color: #333; }
</style>
</head>
<body>
<svg width="0" height="0" style="position:absolute">
  <defs>
    <symbol id="cloud" viewBox="0 0 60 40"><path d="M13 38 A11 11 0 0 1 11 16 A16 16 0 0 1 41 11 A13 13 0 0 1 48 38 Z"/></symbol>
    <symbol id="tick" viewBox="0 0 16 13"><path d="M1 7 L6 12 L15 1 L13 0 L6 8 L3 5 Z" fill="#5fc42a"/></symbol>
  </defs>
</svg>

<div class="page">
  <header>
    <div class="hero" role="img" aria-label="Photo of a businessman touching a glowing cloud outline linked to device icons"></div>
    <div class="hero-fade"></div>
    <span class="brand-dot"></span>
    <div class="brand">Nimbo-Pails.net</div>

    <a class="chat-link" href="#chat">
      <span class="agent" role="img" aria-label="Portrait of a sales agent with headset"></span>
      <span class="box"></span>
      <span class="q">QUESTIONS?</span>
      <span class="pill">CHAT WITH US</span>
    </a>

    <nav class="top-nav">
      <a href="#">OUR COMPANY</a><span class="sep">I</span>
      <a href="#">USE CASES</a><span class="sep">I</span>
      <a href="#">CLOUD SERVICES</a><span class="sep">I</span>
      <a href="#">PAIL'S INFRASTRUCTURE</a><span class="sep">I</span>
      <a href="#">CUSTOMER LOGIN</a>
    </nav>

    <div class="hero-title main">Create your own private cloud, brick by brick.</div>
    <div class="hero-title sub">Each BRICK just $ 990 per month!</div>
  </header>

  <section class="band">
    <div class="feature">
      <div class="badge" style="left:122px"><svg width="30" height="30" viewBox="0 0 30 30"><use href="#cloud" x="1" y="6" width="28" height="19" fill="none" stroke="#fff" stroke-width="4"/></svg></div>
      <h2 style="left:25px">BECOME A CLOUD<br>HOSTING PROVIDER</h2>
      <ul style="left:30px;width:240px">
        <li><svg class="tk" width="16" height="13"><use href="#tick"/></svg>Sell individual virtual machines or complete virtual networks.</li>
        <li><svg class="tk" width="16" height="13"><use href="#tick"/></svg>Start your own hosting business</li>
        <li><svg class="tk" width="16" height="13"><use href="#tick"/></svg>Up to three times cheaper than TGS</li>
        <li><svg class="tk" width="16" height="13"><use href="#tick"/></svg>Free virtual datacenter management software</li>
      </ul>
    </div>
    <div class="feature">
      <div class="badge" style="left:400px"><svg width="30" height="30" viewBox="0 0 30 30" fill="#fff"><rect x="3" y="6" width="6" height="20"/><rect x="12" y="4" width="6" height="22"/><rect x="21" y="6" width="6" height="20"/></svg></div>
      <h2 style="left:303px">VIRTUALIZE YOUR SERVER<br>INFRASTRUCTURE</h2>
      <ul style="left:296px;width:250px">
        <li><svg class="tk" width="16" height="13"><use href="#tick"/></svg>Forget about managing physical servers</li>
        <li><svg class="tk" width="16" height="13"><use href="#tick"/></svg>Just rent the computer capacity you need and send your datacenter to the cloud.</li>
        <li><svg class="tk" width="16" height="13"><use href="#tick"/></svg>Create virtual servers in minutes.</li>
        <li><svg class="tk" width="16" height="13"><use href="#tick"/></svg>Fully redundant and dedicated physical hardware</li>
        <li><svg class="tk" width="16" height="13"><use href="#tick"/></svg>Paneo and Kernix supported</li>
        <li><svg class="tk" width="16" height="13"><use href="#tick"/></svg>Connect your current network to the cloud using out Site to Site VPNs</li>
      </ul>
    </div>
    <div class="feature">
      <div class="badge" style="left:677px"><svg width="30" height="30" viewBox="0 0 30 30"><use href="#cloud" x="1" y="3" width="28" height="19" fill="#fff"/><rect x="9" y="11" width="12" height="3" fill="#0c0c24"/><rect x="9" y="16" width="12" height="3" fill="#0c0c24"/><rect x="9" y="21" width="12" height="5" fill="#fff"/></svg></div>
      <h2 style="left:580px">MOVE FROM PUBLIC TO<br>PRIVATE CLOUD</h2>
      <ul style="left:580px;width:240px">
        <li><svg class="tk" width="16" height="13"><use href="#tick"/></svg>Already spending more than US$ 1.000 per month in the public cloud?</li>
        <li><svg class="tk" width="16" height="13"><use href="#tick"/></svg>Start saving money by creating your own private cloud.</li>
        <li><svg class="tk" width="16" height="13"><use href="#tick"/></svg>Easy to use web based management software</li>
      </ul>
    </div>
  </section>

  <section class="tiles">
    <div class="tile" style="left:43px"><div class="frame"><svg width="58" height="44"><use href="#cloud" width="58" height="40" fill="var(--accent-blue)"/><rect x="17" y="17" width="22" height="14" fill="#fff"/><rect x="19" y="19" width="18" height="10" fill="var(--accent-blue)"/><rect x="14" y="31" width="28" height="3" fill="#fff"/></svg></div><p>Saving money<br>with the private<br>cloud</p></div>
    <div class="tile" style="left:171px"><div class="frame"><svg width="58" height="44"><use href="#cloud" width="58" height="40" fill="var(--accent-blue)"/><circle cx="30" cy="22" r="7" fill="#fff" stroke="#0d3f6e" stroke-width="2"/><path d="M35 27 L42 36" stroke="#0d3f6e" stroke-width="4"/></svg></div><p>Nimbo-Pails<br>technical<br>features</p></div>
    <div class="tile" style="left:300px"><div class="frame"><svg width="58" height="44"><use href="#cloud" width="58" height="40" fill="var(--accent-blue)"/><rect x="21" y="13" width="17" height="21" fill="#fff"/><path d="M24 18h11M24 22h11M24 26h8" stroke="var(--accent-blue)" stroke-width="1.5"/></svg></div><p>Introducing<br>Nimbo-Pails<br>virtual<br>datacenter<br>management<br>platform</p></div>
    <div class="tile" style="left:427px"><div class="frame"><svg width="58" height="44"><use href="#cloud" width="58" height="40" fill="var(--accent-blue)"/><path d="M29 14 L32 22 L40 22 L34 27 L36 35 L29 30 L22 35 L24 27 L18 22 L26 22 Z" fill="#fff"/></svg></div><p>Cloud Services</p></div>
    <div class="tile" style="left:555px"><div class="frame"><svg width="58" height="44"><use href="#cloud" width="58" height="40" fill="var(--accent-blue)"/><circle cx="22" cy="22" r="3.5" fill="#fff"/><circle cx="36" cy="22" r="3.5" fill="#fff"/><circle cx="29" cy="19" r="4" fill="#fff"/><path d="M16 33a6 6 0 0 1 12 0ZM30 33a6 6 0 0 1 12 0ZM22 31a7 7 0 0 1 14 0Z" fill="#fff"/></svg></div><p>7x24x365<br>Support</p></div>
    <div class="tile" style="left:684px"><div class="frame"><svg width="58" height="44"><use href="#cloud" width="58" height="40" fill="var(--accent-blue)"/><rect x="19" y="24" width="5" height="12" fill="#fff"/><path d="M26 24 L30 14 Q33 14 32 20 L38 20 Q40 21 39 24 L37 35 L26 35 Z" fill="#fff"/></svg></div><p>Pricing</p></div>
  </section>

  <footer class="site-footer">
    <h3 style="left:36px">About Nimbo-Pails.net</h3>
    <p class="about">Lorem ipsum dolor sit amet, consectetue adipiscing elit, sed diam nonummy nibh euismod tincidunt ut laoreet dolore mag aliquam erat volutpat. Ut wisi enim admi veniam, quis nostrud exerci tation ullam corper suscipit lobortis nisl ut aliquip ex ea commodo consequat. Duis autem vel eum iriure dolor in hendrerit in vulputa velit esse molestie consequat.</p>

    <h3 style="left:244px">Navigation</h3>
    <ul class="foot-nav">
      <li>Our Company</li><li>Use Cases</li><li>Cloud Services</li><li>Pail's Infrastructure</li><li>Customer Login</li>
    </ul>

    <h3 style="left:370px">Quick Contact</h3>
    <div class="field" style="top:53px">Name</div>
    <div class="field" style="top:77px">Email</div>
    <div class="field" style="top:100px">Phone</div>
    <div class="field" style="top:124px;height:46px">Message</div>
    <div class="send">SEND</div>

    <h3 style="left:566px">Contact Info</h3>
    <ul class="contact" style="top:57px"><li style="position:relative"><svg width="10" height="12" viewBox="0 0 10 12"><path d="M5 0a4 4 0 0 1 4 4c0 3-4 8-4 8S1 7 1 4a4 4 0 0 1 4-4Z" fill="#fff"/><circle cx="5" cy="4" r="1.5" fill="#17164d"/></svg>Lorem Ipsum<br>New York NY</li></ul>
    <ul class="contact" style="top:89px"><li style="position:relative"><svg width="12" height="10" viewBox="0 0 12 10"><path d="M0 3 Q6 -1 12 3 L10 5 L8 3 L4 3 L2 5 Z M2 6h8v4H2Z" fill="#fff"/></svg>123.456.7890</li></ul>
    <ul class="contact" style="top:110px"><li style="position:relative"><svg width="12" height="9" viewBox="0 0 12 9"><rect width="12" height="9" fill="#fff"/><path d="M0 0 L6 5 L12 0" fill="none" stroke="#17164d"/></svg>info@nimbo-pails.net</li></ul>
    <div class="social"><span></span><span></span><span></span></div>

    <span class="foot-brand-dot"></span>
    <div class="foot-brand">Nimbo-Pails.net</div>
  </footer>

  <p class="copyright">COPYRIGHT © 2015 NIMBO-PAILS.NET.&nbsp; ALL RIGHTS RESERVED.</p>
</div>
</body>
</html>
```